Geschäftsunterlagen mit vorhandenem Logo
Zielgruppe
- Immobilienmakler.
- Vermietung und Verkauf von Immobilien
- Eigentümer, Bauträger, Hausverwaltungen, Immobilienentwickler, Wohnungsbaugesellschaften, Käufer und Mieter.
Aufgabenstellung
Wir suchen ein neues Design für unsere Geschäftsunterlagen. Es soll dem Betrachter ein gutes Gefühl vermittelt. Es soll seriös, edel und dynamisch wirken, aber auch vertrauensvoll und kompetent.
Wir suchen neue Designs für folgende Unterlagen, das Logo soll hierbei etwas stärker im Vordergrund stehen :
- Visitenkarten ( Text= Logo, mein Name Jonas Brettler, Handynr. und Webseite )
- Briefpapier ( Text= Logo, Firmenname, Adresse, email, Tel-Nr., event. Bankverbindung ) + Briefumschlag ( Din-Lang ) + email-Vorlage ( Logo + Firmenname, Adresse + Telefon )
- Mappe für Unterlagen ( Din A4 )
- Vermietungsschild und Verkaufsschild fürs Objekt ( 1. H=700mm x B=440mm und 2. H=600 x B 1000mm ) Falls die Schilder zu viel sind, lassen Sie die Entwürfe bitte weg. Priorität haben die anderen Unterlagen.
Logo ist vorhanden, die Schrift kann noch variiert werden.
Falls Sie Fragen haben, schreiben Sie uns bitte an.

```html
<!DOCTYPE html>
<html lang="de">
<head>
<meta charset="utf-8">
<title>Brettler Immobilien – Visitenkarten</title>
<link href="https://fonts.googleapis.com/css2?family=Open+Sans:wght@300;400;600&display=swap" rel="stylesheet">
<style>
  :root {
    --page: #fcfcfc;
    --card: #ffffff;
    --ink: #161616;
    --frame: #111111;
    --mark: #1f4fc4;
    --pale-blue: #d6def3;
    --pale-sky: #e2f3fb;
    --sky: #5cc8f7;
    --mid-blue: #4b9fe6;
    --deep-blue: #0d2ea6;
  }
  * { margin: 0; padding: 0; box-sizing: border-box; }
  html, body { width: 1200px; height: 848px; overflow: hidden; }
  body {
    background: var(--page);
    position: relative;
    font-family: "Open Sans", sans-serif;
    color: var(--ink);
  }
  .card {
    position: absolute;
    background: var(--card);
    overflow: hidden;
  }
  .card--portrait { left: 173px; top: 206px; width: 298px; height: 460px; border: 1px solid var(--frame); }
  .card--landscape { left: 560px; top: 286px; width: 462px; height: 299px; border: 1.5px solid var(--frame); }

  .card__backdrop { position: absolute; }
  .card--portrait .card__backdrop {
    inset: 0;
    background: radial-gradient(ellipse 62% 52% at 55% 48%, var(--card) 0%, var(--card) 62%, var(--pale-sky) 82%, var(--pale-blue) 100%);
  }
  .card--landscape .card__backdrop {
    top: 0; bottom: 0; right: 0; width: 180px;
    background: linear-gradient(to right, rgba(255,255,255,0) 0%, var(--sky) 35%, var(--mid-blue) 65%, var(--deep-blue) 100%);
  }

  .brand { position: absolute; display: flex; align-items: center; gap: 9px; }
  .brand__dot { width: 44px; height: 44px; border-radius: 50%; background: var(--mark); flex: none; }
  .brand__name { font-weight: 600; color: var(--ink); line-height: 1; }
  .brand__word { display: block; font-size: 21px; letter-spacing: 0.3em; }
  .brand__sub { display: block; font-size: 11px; letter-spacing: 0.72em; margin-top: 5px; }
  .card--portrait .brand { left: 67px; top: 112px; }
  .card--landscape .brand { left: 43px; top: 32px; }

  .contact { position: absolute; }
  .contact__name { font-weight: 400; font-size: 24px; letter-spacing: 0.1em; line-height: 1; margin-bottom: 6px; }
  .contact__line { font-weight: 300; font-size: 15.5px; line-height: 21px; }
  .card--portrait .contact { right: 34px; top: 208px; text-align: right; }
  .card--landscape .contact { left: 52px; top: 150px; }
</style>
</head>
<body>

<section class="card card--portrait" aria-label="Visitenkarte hochformat">
  <div class="card__backdrop" role="img" aria-label="Zarter hellblauer Farbverlauf als Hintergrunddekor"></div>
  <div class="brand">
    <span class="brand__dot"></span>
    <span class="brand__name"><span class="brand__word">BRETTLER</span><span class="brand__sub">IMMOBILIEN</span></span>
  </div>
  <div class="contact">
    <p class="contact__name">JONAS BRETTLER</p>
    <p class="contact__line">www.brettler-immo.de</p>
    <p class="contact__line">0176-481 36 907</p>
  </div>
</section>

<section class="card card--landscape" aria-label="Visitenkarte querformat">
  <div class="card__backdrop" role="img" aria-label="Blauer Farbverlauf als Dekor am rechten Rand"></div>
  <div class="brand">
    <span class="brand__dot"></span>
    <span class="brand__name"><span class="brand__word">BRETTLER</span><span class="brand__sub">IMMOBILIEN</span></span>
  </div>
  <div class="contact">
    <p class="contact__name">JONAS BRETTLER</p>
    <p class="contact__line">www.brettler-immo.de</p>
    <p class="contact__line">0176-481 36 907</p>
  </div>
</section>

</body>
</html>
```